National Female Non-profit Business Card

We need a business card design as soon as possible for a non-profit organisation called Meadow to Summit. Our aim is to empower leadership potential in rural female teens.
The business card should have our logo on the one side and then information on the other side, including name, job title, email address, phone number and website (www.meadowtosummit.com.au) and our twitter handle @MeadowSummit
It should use the colours white, coral (#f04a50) and orange (#f68e4e). The font used in the logo is Raleway.
The hashtag #YoungVoicesRise could be used.
It should be bright, chic and crisp. Our logo is attached.

Target Market(s)
We will be handing the cards out to politicians and senior executives. However, as we're a non-profit for young women, they also need to reflect femininity and youth.
Industry/Entity Type
Non-Profit

```html
<!DOCTYPE html>
<html lang="en">
<head>
<meta charset="utf-8">
<title>Meadow to Summit – Business Card</title>
<link rel="stylesheet" href="https://fonts.googleapis.com/css2?family=Raleway:wght@400&family=Inter:wght@300;500&display=swap">
<style>
  :root {
    --backdrop: #eef0f3;
    --card: #ffffff;
    --coral: #f04a50;
    --orange: #f68e4e;
    --ink: #111111;
    --card-edge: #dcdfe4;
  }
  * { box-sizing: border-box; margin: 0; padding: 0; }
  html, body { width: 1200px; height: 1000px; overflow: hidden; }
  body {
    position: relative;
    background: var(--backdrop);
    font-family: "Inter", Arial, sans-serif;
    color: var(--ink);
  }
  .card {
    position: absolute;
    left: 304px;
    width: 592px;
    height: 357px;
    background: var(--card);
    border: 1px solid var(--card-edge);
    border-radius: 16px;
  }
  .card--front { top: 127px; }
  .card--back { top: 516px; }

  .brand-name {
    position: absolute;
    left: 0; right: 0;
    top: 225px;
    text-align: center;
    font-family: "Raleway", Arial, sans-serif;
    font-weight: 400;
    font-size: 22px;
    letter-spacing: 0.3px;
    color: var(--coral);
  }
  .brand-dot {
    display: block;
    width: 18px; height: 18px;
    margin: 0 auto 14px;
    border-radius: 50%;
    background: var(--coral);
  }

  .person {
    position: absolute;
    left: 35px;
    top: 153px;
    padding-left: 21px;
    border-left: 6px solid var(--orange);
    line-height: 1;
  }
  .person__name {
    font-size: 19px;
    font-weight: 300;
    margin-top: -1px;
  }
  .person__name strong { font-weight: 500; }
  .person__role {
    font-size: 16px;
    font-weight: 300;
    margin-top: 7px;
    padding-bottom: 1px;
  }

  .contacts {
    position: absolute;
    left: 28px;
    top: 240px;
    list-style: none;
  }
  .contacts li {
    display: flex;
    align-items: center;
    height: 24.3px;
    font-size: 16px;
    font-weight: 300;
  }
  .contacts svg {
    width: 20px; height: 20px;
    margin-right: 7px;
    flex: none;
  }
  .contacts .marker {
    width: 14px; height: 14px;
    margin: 0 10px 0 3px;
    border-radius: 50%;
    background: var(--orange);
    flex: none;
  }
</style>
</head>
<body>
  <section class="card card--front" aria-label="Card front">
    <p class="brand-name"><span class="brand-dot"></span>MEADOW TO SUMMIT</p>
  </section>

  <section class="card card--back" aria-label="Card back">
    <div class="person">
      <p class="person__name">Clara <strong>Bennett</strong></p>
      <p class="person__role">Director</p>
    </div>

    <ul class="contacts">
      <li>
        <svg viewBox="0 0 20 20" aria-hidden="true" fill="none" stroke="var(--orange)" stroke-width="1.2">
          <circle cx="10" cy="10" r="8.6"/>
          <path d="M7.4 5.2l1.6 2.6-1.1 1c.5 1.4 1.4 2.5 2.7 3.3l1.1-.9 2.5 1.7-1 1.7c-3.4-.6-6.2-3.6-6.8-7.3z" fill="var(--orange)" stroke="none"/>
        </svg>
        0400 555 217
      </li>
      <li>
        <svg viewBox="0 0 20 20" aria-hidden="true">
          <rect x="1" y="4" width="18" height="12.5" rx="1" fill="var(--orange)"/>
          <path d="M1.5 4.5L10 11l8.5-6.5M1.5 16L7.5 9.5M18.5 16l-6-6.5" fill="none" stroke="#fff" stroke-width="1.1"/>
        </svg>
        contact@meadowtosummit.com.au
      </li>
      <li>
        <span class="marker"></span>
        MeadowSummit
      </li>
      <li>
        <svg viewBox="0 0 20 20" aria-hidden="true" fill="none" stroke="var(--orange)" stroke-width="0.9">
          <circle cx="10" cy="10" r="8.6"/>
          <ellipse cx="10" cy="10" rx="4" ry="8.6"/>
          <path d="M10 1.4v17.2M1.4 10h17.2M2.8 5.8h14.4M2.8 14.2h14.4"/>
        </svg>
        meadowtosummit.com.au
      </li>
    </ul>
  </section>
</body>
</html>
```